Redesign for existing homepage

We would like a redesign for our websites 2 column homepage
We provide engine repair and reconditioning services
We would like a cleaner, modern site that works well with our logo colors
Please see the attached brief for more info
Target Market(s)
25 - 45
Industry/Entity Type
Cleaner
Requirements
Must have
- Google Fonts

```html
<!DOCTYPE html>
<html lang="en">
<head>
<meta charset="utf-8">
<title>Marlow Hart Engine Rebuilders</title>
<link rel="stylesheet" href="https://fonts.googleapis.com/css2?family=Jost:wght@400;500;600;700&family=Roboto+Condensed:wght@400;500&display=swap">
<style>
:root{
  --page:#ebebeb;
  --blue:#0a4cff;
  --blue-dark:#0632b3;
  --yellow:#f6e71a;
  --amber:#f6b400;
  --ink:#111;
  --card:#f4f2f2;
  --white:#fff;
}
*{margin:0;padding:0;box-sizing:border-box}
html,body{width:1138px;height:1200px;overflow:hidden}
body{background:var(--page);font-family:"Jost",sans-serif;color:var(--ink);position:relative}
a{text-decoration:none}
.site-header{height:115px;background:linear-gradient(180deg,#2a2a2a,#0d0d0d);position:relative}
.brand{position:absolute;left:172px;top:30px;display:flex;align-items:center;gap:12px}
.brand-dot{width:44px;height:44px;border-radius:50%;background:var(--amber)}
.brand-name{font-weight:600;font-size:25px;line-height:26px;color:var(--amber)}
.social{position:absolute;right:150px;top:10px;display:flex;gap:8px}
.social span{width:30px;height:30px;border-radius:50%;background:#3b6fcf;display:block}
.social span:nth-child(2){background:#2fb2e6}
.social span:nth-child(3){background:#1e88c9}
.header-phone{position:absolute;right:151px;top:70px;display:flex;align-items:center;gap:6px;color:var(--white);font-family:"Roboto Condensed",sans-serif;font-weight:500;font-size:29px}
.main-nav{height:33px;background:var(--blue);display:flex;justify-content:center}
.main-nav a{color:var(--white);font-family:"Roboto Condensed",sans-serif;font-size:16px;line-height:33px;padding:0 14px;border-left:1px solid rgba(255,255,255,.35)}
.main-nav a:first-child{border-left:none}
.page{position:absolute;left:131px;top:148px;width:877px;height:928px;background:var(--white)}
.hero{height:220px;background:linear-gradient(90deg,#b9b5ad 0%,#6c6c70 35%,#8b8a88 60%,#d8d8d6 100%)}
.intro{position:absolute;left:25px;top:258px;width:565px}
.intro h1{font-weight:400;font-size:26px;line-height:30px;margin-bottom:8px;white-space:nowrap}
.intro p{font-size:12px;line-height:20px}
.card{position:absolute;width:236px;height:226px;background:var(--card);border-top:3px solid var(--amber);padding:11px 11px 0}
.card h2{font-family:"Roboto Condensed",sans-serif;font-weight:400;font-size:20px;white-space:nowrap;display:flex;align-items:center;justify-content:center;gap:5px;height:26px}
.card h2::before,.card h2::after{content:"";flex:none;width:28px;height:9px;background:repeating-linear-gradient(180deg,var(--blue) 0 1.5px,transparent 1.5px 3.5px)}
.card-img{height:90px;margin-top:10px}
.card p{font-size:13px;line-height:16px;text-align:center;margin-top:7px}
.btn{display:block;margin:9px auto 0;width:131px;height:33px;background:var(--blue);border-bottom:3px solid var(--blue-dark);border-radius:3px;color:var(--white);font-size:11px;text-align:center;line-height:31px}
.btn svg{vertical-align:middle;margin-left:2px}
.sidebar{position:absolute;left:632px;width:219px;display:block}
.quote{top:262px;height:78px;background:linear-gradient(180deg,#f8c21d,#f1a91a);border:2px solid #e28a2c;color:#fff3b0;font-weight:700;font-size:19px;line-height:23px;text-align:center;padding-top:14px;white-space:nowrap}
.stockist{top:354px;height:166px;background:var(--yellow);text-align:center;padding-top:8px}
.stockist .badge{width:74px;height:85px;margin:0 auto;border:1.5px solid #222}
.stockist p{font-size:18px;line-height:24px;margin-top:6px;white-space:nowrap}
.member{top:540px;height:166px;background:linear-gradient(135deg,#1458ff,#0a46f0);text-align:center;color:var(--white);padding-top:14px}
.member .badge{width:102px;height:62px;border-radius:50%;background:#0c0c0c;margin:0 auto;border:1px solid #fff}
.member p{font-family:"Roboto Condensed",sans-serif;font-size:17px;line-height:21px;margin-top:11px;white-space:nowrap}
.contact{top:725px}
.contact h3{background:var(--yellow);height:37px;font-family:"Roboto Condensed",sans-serif;font-weight:400;font-size:22px;line-height:40px;text-align:center}
.contact-body{background:#000;color:var(--white);height:130px;padding:6px 0 0 30px;font-family:"Roboto Condensed",sans-serif;font-size:17px;line-height:21px}
.contact-row{display:flex;gap:10px;align-items:flex-start}
.contact-row svg{margin-top:3px;flex:none}
.site-footer{position:absolute;left:0;top:1076px;width:1138px;height:124px;background:linear-gradient(180deg,#2a3640,#141c22)}
.footer-nav{display:flex;justify-content:center;gap:30px;padding-top:19px}
.footer-nav a{color:var(--white);font-family:"Jost",sans-serif;font-weight:500;font-size:12px}
.copyright{text-align:center;color:#d8d8d8;font-size:12px;margin-top:50px}
</style>
</head>
<body>
<header class="site-header">
  <div class="brand"><span class="brand-dot"></span><span class="brand-name">Marlow Hart<br>Engine Rebuilders</span></div>
  <div class="social"><span></span><span></span><span></span></div>
  <div class="header-phone">
    <svg width="34" height="34" viewBox="0 0 24 24"><path fill="#f6d400" d="M6.6 10.8c1.4 2.8 3.8 5.1 6.6 6.6l2.2-2.2c.3-.3.7-.4 1-.2 1.1.4 2.3.6 3.6.6.6 0 1 .4 1 1V20c0 .6-.4 1-1 1C10.6 21 3 13.4 3 4c0-.6.4-1 1-1h3.5c.6 0 1 .4 1 1 0 1.3.2 2.5.6 3.6.1.3 0 .7-.2 1z"/><path fill="none" stroke="#f6d400" stroke-width="1.6" d="M14 3a7 7 0 0 1 7 7M14 6.5a3.5 3.5 0 0 1 3.5 3.5"/></svg>
    (04) 555 0142
  </div>
</header>
<nav class="main-nav">
  <a href="#">Home</a><a href="#">About Us</a><a href="#">Private Vehicle Service &amp; Repair</a><a href="#">Trade Customers</a><a href="#">Race &amp; Classic Car Engines</a><a href="#">Make an Enquiry</a><a href="#">Contct Us</a>
</nav>
<main class="page">
  <div class="hero" role="img" aria-label="Car raised on a workshop hoist beside a rebuilt engine"></div>
  <section class="intro">
    <h1>Welcome to Marlow Hart Engine Rebuilders</h1>
    <p>Lorem Ipsum. Proin gravida nibh vel velit auctor aliquet. Aenean sollicitudin, lorem quis bibendum auctor, nisi elit consequat ipsum, nec sagittis sem nibh id elit. Duis sed odio sit amet nibh vulputate cursus a sit amet mauris. Morbi accumsan ipsum velit. Nam nec tellus a odio tincidunt auctor a ornare odio. Sed non&nbsp; mauris vitae erat consequat auctor eu in elit..</p>
  </section>

  <article class="card" style="left:26px;top:416px">
    <h2>Service Car Engine</h2>
    <div class="card-img" role="img" aria-label="Mechanic checking a steaming engine bay" style="background:linear-gradient(135deg,#8c8d86,#4a4b47 60%,#a9a9a2)"></div>
    <p>Lorem Ipsum. Proin gravida nibh vel velit auctor aliquet.</p>
    <a class="btn" href="#">Learn more<svg width="18" height="8" viewBox="0 0 18 8"><path d="M0 4h15M12 1l4 3-4 3" stroke="#f6c400" stroke-width="1.6" fill="none"/></svg></a>
  </article>
  <article class="card" style="left:328px;top:416px">
    <h2>Trade Customers</h2>
    <div class="card-img" role="img" aria-label="Engineering workshop with machining equipment" style="background:linear-gradient(135deg,#6f7c62,#8a9a78 50%,#b0a890)"></div>
    <p>Lorem Ipsum. Proin gravida nibh vel velit auctor aliquet.</p>
    <a class="btn" href="#">Learn more<svg width="18" height="8" viewBox="0 0 18 8"><path d="M0 4h15M12 1l4 3-4 3" stroke="#f6c400" stroke-width="1.6" fill="none"/></svg></a>
  </article>
  <article class="card" style="left:26px;top:677px">
    <h2>Race &amp; Classic Car</h2>
    <div class="card-img" role="img" aria-label="Chrome and orange race engine close-up" style="background:linear-gradient(135deg,#2a2e3a,#7b7f88 45%,#b0482a 75%,#3a3a40)"></div>
    <p>Lorem Ipsum. Proin gravida nibh vel velit auctor aliquet.</p>
    <a class="btn" href="#">Learn more<svg width="18" height="8" viewBox="0 0 18 8"><path d="M0 4h15M12 1l4 3-4 3" stroke="#f6c400" stroke-width="1.6" fill="none"/></svg></a>
  </article>
  <article class="card" style="left:322px;top:677px">
    <h2>Make an Enquiry</h2>
    <div class="card-img" role="img" aria-label="Cylinder head with rows of valves" style="background:linear-gradient(180deg,#6b6462,#a39c98 50%,#e2dfdc)"></div>
    <p>Lorem Ipsum. Proin gravida nibh vel velit auctor aliquet.</p>
    <a class="btn" href="#">Learn more<svg width="18" height="8" viewBox="0 0 18 8"><path d="M0 4h15M12 1l4 3-4 3" stroke="#f6c400" stroke-width="1.6" fill="none"/></svg></a>
  </article>

  <a class="sidebar quote" href="#">GET A FREE QUOTE<br>FOR ENGINE WORK</a>
  <aside class="sidebar stockist">
    <div class="badge"></div>
    <p>Official stockists of<br>Southern Cylinder Heads</p>
  </aside>
  <aside class="sidebar member">
    <div class="badge"></div>
    <p>As members of the ERA Guild,<br>you can rely on us to get the<br>job done right, first time!</p>
  </aside>
  <aside class="sidebar contact">
    <h3>CONTACT INFO</h3>
    <div class="contact-body">
      <div class="contact-row"><svg width="14" height="20" viewBox="0 0 14 20"><path d="M7 1a6 6 0 0 1 6 6c0 4.5-6 12-6 12S1 11.5 1 7a6 6 0 0 1 6-6z" fill="none" stroke="#ccc" stroke-width="1.6"/><circle cx="7" cy="7" r="2.2" fill="#ccc"/></svg><span>128 Harbour Road,<br>Eastbay, Wellington.</span></div>
      <div class="contact-row" style="margin-top:21px"><svg width="15" height="13" viewBox="0 0 15 13"><path d="M1 4c0-2 13-2 13 0v1h-3V3.5h-7V5H1z M3 6h9l2 6H1z" fill="#ccc"/></svg><span>(04) 555 0142</span></div>
      <div class="contact-row"><svg width="15" height="15" viewBox="0 0 15 15"><rect x="4" y="1" width="7" height="4" fill="#ccc"/><rect x="1" y="6" width="13" height="6" rx="1" fill="#ccc"/><rect x="4" y="10" width="7" height="4" fill="#888"/></svg><span>(04) 555 0178</span></div>
    </div>
  </aside>
</main>
<footer class="site-footer">
  <nav class="footer-nav">
    <a href="#">Home</a><a href="#">About Us</a><a href="#">Private Vehicle Service &amp; Repair</a><a href="#">Trade Customers</a><a href="#">Race &amp; Classic Car Engines</a><a href="#">Make an Enquiry</a><a href="#">Contct Us</a>
  </nav>
  <p class="copyright">Copyright © 2014 Marlow Hart Engine Rebuilders | All Rights Reserved.</p>
</footer>
</body>
</html>
```